Flyer - Clearway Dental Marrowby

** Please do not use my words - word-for-word on the flyer design **
We have recently bought an established dental business. However we are not getting new customers through the door. We plan to implement aggressive local marketing strategies including flyer distribution. We are looking for an eye-catching must read flyer design. Some details & content ideas are as below.
1. A5 size - Double Sided
2. Our business name is Clearway Dental Marrowby. Logo is attached. Website is www.clearwaydentalmarrowby.example.au where lot of useful information can be found.
3. Practice has a long & proud history serving "Lower North Shore" since 1958. We provide quality dental care at affordable prices.
4. List of services can be found on website
5. Perhaps a snippet of Orbix Map Location would be useful. Also the fact that 3-hour free parking is available in Ferncroft Arcade less than 100m away from practice. Plenty of 2-hours street parking is available too.
6. Opening hours can be found on website. Fact that we are open on Saturdays and till late on Tuesdays is worth calling out.
7. We would like to run a campaign of offers with this flyer. Give it a name! Details below.
a) NO GAP Checkup and Clean with any major Private Health Fund. Includes oral exam, 2 X-Rays, Scale & Polish and Fluoride Treatment
b) Genuine Teeth Whitening for $199 (usually $399 save $200)
c) 10% off on all major dental. Includes fillings, crowns, bridges and root canal treatment
8. We are KEVO Preferred Provider means KEVO members get maximum benefit. KEVO Patient Circle logo attached.
9. We participate in Office of Civic Pensions Fee Schedule. Logo attached.
10. Call out WE ACCEPT ALL HEALTH FUNDS
Dental
- Helvetica Neue, Myriad Pro

```html
<!DOCTYPE html>
<html lang="en">
<head>
<meta charset="utf-8">
<title>Clearway Dental Marrowby – Flyer</title>
<link rel="stylesheet" href="https://fonts.googleapis.com/css2?family=Oswald:wght@500;600&family=Teko:wght@400&family=Lato:wght@700;900&family=Arimo:wght@400;700&display=swap">
<style>
  :root {
    --teal-dark: #245868;
    --mint: #2dd48f;
    --lime: #c7e94b;
    --lime-text: #d8f23f;
    --hours-green: #95c11f;
    --ink: #2c2c2c;
    --paper: #ffffff;
    --backdrop: #e9ecec;
  }
  html, body {
    margin: 0;
    width: 900px;
    height: 1200px;
    overflow: hidden;
    background: var(--backdrop);
  }
  .flyer {
    position: absolute;
    left: 27px;
    top: 0;
    width: 695px;
    height: 985px;
    background: var(--paper);
    transform: scale(1.2183);
    transform-origin: top left;
    overflow: hidden;
    font-family: "Arimo", Arial, sans-serif;
  }
  .family-photo {
    position: absolute;
    left: 305px; top: 0;
    width: 390px; height: 300px;
    background: linear-gradient(120deg, #e9d3bf 0%, #d9b394 35%, #c9a88a 60%, #b9bcc0 100%);
  }
  .ribbon, .footer-wave { position: absolute; left: 0; top: 0; }
  .logo-badge {
    position: absolute;
    left: 105px; top: 25px;
    width: 150px; height: 150px;
    border-radius: 50%;
    background: var(--teal-dark);
    display: flex; flex-direction: column;
    align-items: center; justify-content: center;
    color: var(--mint);
    font-family: "Lato", Arial, sans-serif;
    font-weight: 700;
    font-size: 19px;
    line-height: 1.15;
    text-align: center;
  }
  .headline {
    position: absolute;
    left: 43px; top: 286px;
    margin: 0;
    font-family: "Oswald", Arial, sans-serif;
    font-weight: 600;
    text-transform: uppercase;
    color: var(--teal-dark);
    line-height: 1;
  }
  .headline .big { display: block; font-size: 56px; letter-spacing: 0.5px; }
  .headline .mid { display: block; font-size: 27px; color: var(--mint); margin-top: 6px; }
  .headline .low { display: block; font-size: 34px; margin-top: 6px; }
  .offer-box {
    position: absolute;
    left: 455px; top: 340px;
    width: 213px; height: 275px;
    background: var(--mint);
    border-radius: 0 0 18px 18px;
    text-align: center;
    font-family: "Lato", Arial, sans-serif;
    font-weight: 900;
  }
  .offer-box .label { color: #fff; font-size: 21px; line-height: 1.05; margin-top: 55px; }
  .offer-box .label.lg { font-size: 25px; margin-top: 0; }
  .offer-box .now { color: var(--lime-text); font-size: 44px; line-height: 1; margin-top: 18px; }
  .offer-box .price { color: var(--lime-text); font-size: 74px; line-height: 1; }
  .services-tab {
    position: absolute;
    left: -5px; top: 460px;
    width: 250px; height: 44px;
    background: var(--lime);
    border-radius: 0 22px 22px 0;
    font-family: "Lato", Arial, sans-serif;
    font-weight: 900;
    font-size: 25px;
    color: var(--teal-dark);
    line-height: 44px;
    padding-left: 35px;
    box-sizing: border-box;
  }
  .service-list {
    position: absolute;
    top: 518px;
    margin: 0; padding: 0;
    list-style: none;
    font-family: "Teko", "Arial Narrow", sans-serif;
    font-size: 21px;
    line-height: 24px;
    text-transform: uppercase;
    color: var(--ink);
  }
  .service-list li::before { content: "•"; margin-right: 7px; }
  .service-list.col-a { left: 38px; }
  .service-list.col-b { left: 235px; }
  .hours-title {
    position: absolute; left: 37px; top: 641px;
    font-family: "Lato", Arial, sans-serif; font-weight: 700;
    font-size: 19px; color: var(--mint); margin: 0;
  }
  .hours {
    position: absolute; left: 50px; top: 668px;
    margin: 0; font-size: 18px; line-height: 23.5px;
  }
  .hours dt { color: var(--ink); }
  .hours dd { margin: 0; color: var(--hours-green); font-family: "Oswald", Arial, sans-serif; font-weight: 500; font-size: 17px; }
  .no-gap {
    position: absolute; right: 37px; top: 642px;
    margin: 0; text-align: right;
    font-size: 15.5px; line-height: 21px; color: var(--ink);
  }
  .discount {
    position: absolute; left: 380px; top: 742px; width: 310px;
    text-align: center; color: var(--ink);
  }
  .discount .pct { font-size: 32px; font-weight: 700; color: var(--teal-dark); line-height: 1; }
  .discount p { margin: 10px 0 0; font-size: 16.5px; font-weight: 700; line-height: 21px; }
  .site-url {
    position: absolute; left: 0; top: 910px; width: 695px;
    text-align: center; color: #fff;
    font-family: "Lato", Arial, sans-serif; font-weight: 700; font-size: 29px;
  }
</style>
</head>
<body>
<main class="flyer">
  <div class="family-photo" role="img" aria-label="Photo of a smiling family of four with two young children"></div>

  <svg class="ribbon" width="695" height="400" viewBox="0 0 695 400" aria-hidden="true">
    <path d="M0,150 C130,125 250,160 340,215 C440,275 570,282 695,280 L695,305 C570,310 440,305 340,250 C250,195 130,170 0,180 Z" fill="var(--lime)"/>
    <path d="M0,108 C130,90 230,130 310,190 C400,258 480,300 695,305 L695,372 L455,372 C390,340 340,290 290,245 C210,175 110,135 0,138 Z" fill="var(--mint)"/>
  </svg>

  <div class="logo-badge">Clearway Dental<br>Marrowby</div>

  <h1 class="headline">
    <span class="big">We Provide</span>
    <span class="mid">Quality Dentalcare at</span>
    <span class="low">Affordable Prices</span>
  </h1>

  <div class="offer-box">
    <div class="label">GENUINE TEETH</div>
    <div class="label lg">WHITENING</div>
    <div class="now">Now at</div>
    <div class="price">$199</div>
  </div>

  <div class="services-tab">OUR SERVICES</div>
  <ul class="service-list col-a">
    <li>Checkup &amp; Clean</li>
    <li>Child Friendly Dentistry</li>
    <li>Crowns</li>
    <li>Dentures</li>
    <li>Extraction</li>
  </ul>
  <ul class="service-list col-b">
    <li>Root Canal Treatment</li>
    <li>Same Day Emergency</li>
    <li>Tooth Replacement (Bridges)</li>
    <li>White Fillings</li>
    <li>Whitening</li>
  </ul>

  <h2 class="hours-title">OFFICE HOURS:</h2>
  <dl class="hours">
    <dt>Monday</dt><dd>8:30am - 5:30pm</dd>
    <dt>Tuesday</dt><dd>12:00pm - 8:00pm</dd>
    <dt>Wednesday – Friday</dt><dd>8:30am – 5:30pm</dd>
    <dt>Saturday</dt><dd>9:00am – 4:00pm</dd>
  </dl>

  <p class="no-gap">NO GAP Checkup and Clean<br>with any major Private Health Fund.<br>Includes oral exam, 2 X-Rays,<br>Scale &amp; Polish and Fluoride Treatment</p>

  <div class="discount">
    <div class="pct">10% OFF</div>
    <p>on all major dental Includes<br>fillings, crowns,bridges and root<br>canal treatment</p>
  </div>

  <svg class="footer-wave" width="695" height="985" viewBox="0 0 695 985" aria-hidden="true">
    <path d="M0,895 C200,850 480,850 695,895 L695,985 L0,985 Z" fill="var(--lime)"/>
    <path d="M0,918 C220,876 480,876 695,915 L695,985 L0,985 Z" fill="var(--mint)"/>
  </svg>
  <div class="site-url">www.clearwaydentalmarrowby.example.au</div>
</main>
</body>
</html>
```